Velmor Stationery Design

We need Business Card, Letterhead, #10 Envelope , 3" x 4" Mailing Label, and email signature block. Also need "Aircraft Services" added small under the logo on everything except the email signature block. "Aircraft Services" should be in a simple font to to conflict with or distract from the logo. Our address info is:
4817 Halvend Loop NW
Brantwick, GA 30592
P 555.208.3146
C 555.208.3146 (for biz cards only)
glen@velmorjet.example (for biz cards only)
Website velmorjet.example
Feel free to play around with colors but I expect that black or gray will work best for the address/phone info etc.

Target Market(s)

Aircraft owners

Industry/Entity Type

Aviation

Colors

Designer to choose only greyscale colors for use in the design.

Requirements
Must have
• Clean and sophisticated design -

```html
<!DOCTYPE html>
<html lang="en">
<head>
<meta charset="utf-8">
<title>Velmor Aircraft Services – Business Card</title>
<link rel="stylesheet" href="https://fonts.googleapis.com/css2?family=Montserrat:wght@400;500;700&display=swap">
<style>
  :root {
    --page-bg: #d9d5cf;
    --card-face: #ebe9e6;
    --panel-dark: #1f1f20;
    --accent-blue: #2b6597;
    --edge-cream: #cfc4b0;
    --panel-text: #d9cdb8;
    --brand-text: #2b6597;
  }
  * { margin: 0; padding: 0; box-sizing: border-box; }
  html, body {
    width: 1200px;
    height: 1047px;
    overflow: hidden;
    background: var(--page-bg);
    font-family: "Montserrat", Arial, sans-serif;
  }
  .business-card {
    position: absolute;
    left: 75px;
    top: 236px;
    width: 1050px;
    height: 574px;
    border-radius: 26px;
    overflow: hidden;
    background: var(--card-face);
    box-shadow: 0 10px 30px rgba(0,0,0,0.12);
  }
  .card-shapes {
    position: absolute;
    inset: 0;
    width: 100%;
    height: 100%;
  }
  .brand {
    position: absolute;
    left: 48px;
    top: 62px;
    color: var(--brand-text);
  }
  .brand-name {
    font-size: 78px;
    font-weight: 700;
    letter-spacing: 2px;
    line-height: 1;
  }
  .brand-tagline {
    margin-top: 6px;
    font-size: 33px;
    font-weight: 400;
    letter-spacing: 0.5px;
    line-height: 1;
  }
  .contact-block {
    position: absolute;
    right: 54px;
    top: 186px;
    text-align: right;
    color: var(--panel-text);
  }
  .person-name {
    font-size: 32px;
    font-weight: 700;
    letter-spacing: 1px;
    color: var(--accent-blue);
    line-height: 1.1;
  }
  .person-title {
    margin-top: 6px;
    font-size: 26px;
    font-weight: 500;
    line-height: 1.2;
  }
  .contact-list {
    list-style: none;
    margin-top: 30px;
  }
  .contact-list li {
    display: flex;
    justify-content: flex-end;
    align-items: center;
    gap: 8px;
    font-size: 25px;
    line-height: 36px;
  }
  .contact-icon {
    width: 20px;
    height: 20px;
    fill: var(--accent-blue);
    flex: none;
  }
  .address {
    margin-top: 18px;
    font-size: 25px;
    line-height: 36px;
    font-style: normal;
    margin-right: 28px;
  }
  .name-marker {
    position: absolute;
    right: 0;
    top: 196px;
    width: 31px;
    height: 72px;
    background: var(--accent-blue);
  }
</style>
</head>
<body>
  <div class="business-card">
    <svg class="card-shapes" viewBox="0 0 878 480" preserveAspectRatio="none" aria-hidden="true">
      <path class="dark-panel" fill="#1f1f20"
            d="M585,0 C625,45 612,115 560,185 C482,292 352,335 330,480 L878,480 L878,0 Z"/>
      <path class="panel-edge" fill="none" stroke="#cfc4b0" stroke-width="2"
            d="M585,0 C625,45 612,115 560,185 C482,292 352,335 330,480"/>
      <path class="blue-sweep" fill="#2b6597"
            d="M598,22 C624,80 598,150 545,212 C468,302 345,350 326,425 C352,345 478,300 556,220 C606,166 622,92 598,22 Z"/>
    </svg>

    <div class="brand">
      <div class="brand-name">VELMOR</div>
      <div class="brand-tagline">AIRCRAFT SERVICES</div>
    </div>

    <div class="name-marker"></div>

    <div class="contact-block">
      <div class="person-name">MARCUS HALE</div>
      <div class="person-title">Managing Director</div>
      <ul class="contact-list">
        <li>555.208.3146
          <svg class="contact-icon" viewBox="0 0 24 24"><path d="M6.6 10.8a15 15 0 0 0 6.6 6.6l2.2-2.2a1 1 0 0 1 1-.25 11.4 11.4 0 0 0 3.6.57 1 1 0 0 1 1 1V20a1 1 0 0 1-1 1A17 17 0 0 1 3 4a1 1 0 0 1 1-1h3.5a1 1 0 0 1 1 1c0 1.25.2 2.45.57 3.57a1 1 0 0 1-.25 1z"/></svg>
        </li>
        <li>555.208.3146
          <svg class="contact-icon" viewBox="0 0 24 24"><path d="M7 1h10a2 2 0 0 1 2 2v18a2 2 0 0 1-2 2H7a2 2 0 0 1-2-2V3a2 2 0 0 1 2-2zm0 3v14h10V4zm5 15.5a1.2 1.2 0 1 0 0 2.4 1.2 1.2 0 0 0 0-2.4z"/></svg>
        </li>
        <li>glen@velmorjet.example
          <svg class="contact-icon" viewBox="0 0 24 24"><path d="M2 5h20v2l-10 6L2 7zm0 4.3 10 6 10-6V19H2z"/></svg>
        </li>
        <li>www.velmorjet.example
          <svg class="contact-icon" viewBox="0 0 24 24"><circle cx="12" cy="12" r="10"/><path d="M2 12h20M12 2c3 3 3 17 0 20M12 2c-3 3-3 17 0 20" stroke="#1f1f20" stroke-width="1.5" fill="none"/></svg>
        </li>
      </ul>
      <address class="address">
        4817 Halvend Loop NW<br>
        Brantwick, GA 30592
      </address>
    </div>
  </div>
</body>
</html>
```